Award winning Indie press looking for a world class book cover for global relaunch

We need to update a book cover for one of our titles which is being relaunched. The title will exist in both physical and e-formats.
There are two primary targets for this book:
1- the coming of age story coupled with the element of forbidden love between a local boy and a British girl
2- the political division of a British colony in the 1950's
Size: A5
Spine: .777 inches or 19.73mm
Title: Hither and Yonder (you may substitute 'and' with '&')
Author: Evangelos K. Drakoulides
Translated by Helen Marsh-Tolley
Blurb: You see before you the entire social mosaic of Cyprus in the ‘50s. - Proinopistis
Publisher: logo- provided
Back cover text:
The touching story of a teenager who struggles with the eternal problems of adolescence, Hither & Yonder is a coming-of-age novel set in a politically divided country.
While the era of British colonialism in Cyprus is coming to a violent end, Dimitri tries to come to terms with the consequences of the political turmoil on his own life. Strengthened by his passion for medieval poetry and his love for the history of his island, he sets out to balance the Cypriot and English elements in his daily life. His quest for answers is complicated by romantic love for his British friend Anne and his physical attraction to his father’s maid Phrossou. Balancing between different identities, religion and communities, his personal search becomes symbolic of his country’s turbulent political situation.
A nostalgic story about family, love and friendship, Hither & Yonder is a powerful novel about the psychology of an adolescent torn between different worlds, and about the complexities of life and love in the social and historical mosaic of 1950’s colonial Cyprus. It is a beautifully-observed, historically-informed novel by the celebrated Greek historian and novelist.
Other: Please allow a box of approximately 2cm height X 3 cm length for the bar code.
Updates
Hi
I've added two images that could be of some help to you.
Hope they help.
Reason: Appreciating the specific difficulties of this design, it's best to have a few more days
Hi
Please amend front cover blurb to the following:
"This is a novel to be read in one go. A charming narrative…and unexpected turns. It keeps the reader in constant suspense". Grafima Monthly Literary Review
Target Market(s)
1 - Adults reading coming of age novels
2 - Adults reading historical fiction on British colonialism
Industry/Entity Type
Political
Colors
Designer to choose colors to be used in the design.
Look and feel
Each slider illustrates characteristics of the customer's brand and the style your logo design should communicate.

```html
<!DOCTYPE html>
<html lang="en">
<head>
<meta charset="utf-8">
<title>Hither &amp; Yonder — Cover Spread</title>
<link rel="stylesheet" href="https://fonts.googleapis.com/css2?family=Sorts+Mill+Goudy:ital@0;1&family=Open+Sans:ital,wght@0,400;0,600;1,400&display=swap">
<style>
  :root {
    --page-bg: #efefef;
    --wall-light: #e6dccb;
    --wall-mid: #cdbfa6;
    --wall-dark: #8f8068;
    --ground-dark: #4a4036;
    --brand-red: #d0232a;
    --title-brown: #4b3b2c;
    --amp-tan: #a08a70;
    --ink: #2f2a25;
    --paper: #fbf9f5;
    --white: #ffffff;
  }
  * { box-sizing: border-box; margin: 0; padding: 0; }
  html, body { width: 1200px; height: 1200px; overflow: hidden; }
  body { background: var(--page-bg); font-family: "Open Sans", sans-serif; }

  .canvas { position: relative; width: 1200px; height: 1200px; }

  .spread {
    position: absolute; left: 30px; top: 221px;
    width: 1140px; height: 758px;
    display: flex;
    box-shadow: 0 6px 22px rgba(0,0,0,0.18);
  }

  .back-cover, .spine, .front-cover { position: relative; height: 100%; overflow: hidden; }
  .back-cover { width: 534px; }
  .spine { width: 72px; }
  .front-cover { width: 534px; }

  .wall-photo {
    position: absolute; inset: 0;
    background:
      radial-gradient(ellipse at 30% 25%, rgba(255,250,240,0.55), transparent 60%),
      linear-gradient(180deg, var(--wall-light) 0%, var(--wall-mid) 55%, var(--wall-dark) 88%, var(--ground-dark) 100%);
  }
  .spine .wall-photo {
    background: linear-gradient(180deg, #eee6d8 0%, #d8ccb6 60%, #9c8d74 90%, #57493c 100%);
  }
  .bicycles-photo {
    position: absolute; left: 30px; right: 0; top: 430px; height: 215px;
    background: radial-gradient(ellipse at 55% 60%, rgba(70,55,40,0.35), transparent 70%);
  }

  .publisher-band {
    position: absolute; height: 40px;
    background: var(--brand-red);
    color: var(--white);
    font-family: "Open Sans", sans-serif; font-weight: 400;
    font-size: 24px; letter-spacing: 2px;
    display: flex; align-items: center; padding-left: 16px;
  }
  .front-cover .publisher-band { left: 0; top: 70px; width: 152px; }

  .title-amp {
    position: absolute; left: 62px; top: 112px;
    font-family: "Sorts Mill Goudy", serif; font-size: 170px; line-height: 1;
    color: var(--amp-tan);
  }
  .title-words {
    position: absolute; left: 172px; top: 100px;
    font-family: "Sorts Mill Goudy", serif; font-size: 58px; line-height: 0.95;
    color: var(--title-brown);
  }
  .review-quote {
    position: absolute; left: 92px; top: 294px; width: 340px;
    font-size: 17px; line-height: 1.3; color: var(--ink);
  }
  .review-quote cite { display: block; font-style: italic; margin-top: 4px; }

  .credit-band {
    position: absolute; left: 16px; right: 0; bottom: 26px; height: 62px;
    background: var(--brand-red);
    color: var(--white);
    font-family: "Sorts Mill Goudy", serif; font-size: 24px; line-height: 1.1;
    padding: 7px 0 0 22px;
  }

  .blurb-panel {
    position: absolute; left: 46px; top: 46px; width: 438px; height: 545px;
    background: var(--paper);
    border: 2px solid var(--brand-red);
    border-radius: 18px;
  }
  .back-cover .publisher-band { left: 0; top: 138px; width: 143px; height: 39px; font-size: 22px; }
  .back-title {
    position: absolute; left: 170px; top: 137px;
    font-family: "Sorts Mill Goudy", serif; font-size: 32px; color: var(--title-brown);
  }
  .back-copy {
    position: absolute; left: 66px; top: 190px; width: 400px;
    font-size: 11.6px; line-height: 1.5; color: var(--ink);
  }
  .back-copy p + p { margin-top: 12px; }
</style>
</head>
<body>
<main class="canvas">
  <section class="spread">

    <div class="back-cover">
      <div class="wall-photo" role="img" aria-label="Sepia photograph of a weathered plaster wall with bare branches along the top edge"></div>
      <div class="blurb-panel"></div>
      <div class="publisher-band">KESTREL</div>
      <h2 class="back-title">Hither &amp; Yonder</h2>
      <div class="back-copy">
        <p>The touching story of a teenager who struggles with the eternal problems of adolescence, Hither &amp; Yonder is a coming-of-age novel set in a politically divided country.</p>
        <p>While the era of British colonialism in Cyprus is coming to a violent end, Dimitri tries to come to terms with the consequences of the political turmoil on his own life. Strengthened by his passion for medieval poetry and his love for the history of his island, he sets out to balance the Cypriot and English elements in his daily life. His quest for answers is complicated by romantic love for his British friend Anne and his physical attraction to his father’s maid Phrossou. Balancing between different identities, religion and communities, his personal search becomes symbolic of his country’s turbulent political situation.</p>
        <p>A nostalgic story about family, love and friendship, Hither &amp; Yonder is a powerful novel about the psychology of an adolescent torn between different worlds, and about the complexities of life and love in the social and historical mosaic of 1950’s colonial Cyprus. It is a beautifully-observed, historically-informed novel by the celebrated Greek historian and novelist.</p>
      </div>
    </div>

    <div class="spine">
      <div class="wall-photo" role="img" aria-label="Continuation of the sepia plaster wall photograph across the spine"></div>
    </div>

    <div class="front-cover">
      <div class="wall-photo" role="img" aria-label="Sepia photograph of a weathered plaster wall with bare branches"></div>
      <div class="bicycles-photo" role="img" aria-label="Vintage bicycles with baskets leaning against the wall in warm sunlight"></div>
      <div class="publisher-band">KESTREL</div>
      <div class="title-amp" aria-hidden="true">&amp;</div>
      <h1 class="title-words">Hither<br>Yonder</h1>
      <blockquote class="review-quote">
        “This is a novel to be read in one go. A charming narrative…and unexpected turns. It keeps the reader in constant suspense”.
        <cite>Grafima Monthly Literary Review</cite>
      </blockquote>
      <div class="credit-band">Evangelos K. Drakoulides<br>Translated by Helen Marsh-Tolley</div>
    </div>

  </section>
</main>
</body>
</html>
```